Copperfox Billboard

Please design a billboard using my photos and logos.
For photo of truck please crop the truck itself out and not have the trees / dirt in photo.
Please put " Best Prices in Sevier County"
Please put " 30-yard Dumpsters Starting at 600.00"
Please put " 16-yard Dumpsters Starting at 300.0"
Please put " Delivery and Pickup 7 Days a week"
Billboard size will be 10 ft tall 30 ft wide

```html
<!DOCTYPE html>
<html lang="en">
<head>
<meta charset="utf-8">
<title>Copperfox Dumpsters Billboard</title>
<link href="https://fonts.googleapis.com/css2?family=Poppins:wght@600;800;900&display=swap" rel="stylesheet">
<style>
  :root {
    --stage: #e8e9ec;
    --ink: #0b0b0c;
    --purple: #5b2a86;
    --purple-deep: #2f1644;
    --purple-bright: #8a47c2;
    --silver: #d9d9d9;
    --panel: #d4d4d4;
    --panel-light: #ececec;
  }
  * { margin: 0; padding: 0; box-sizing: border-box; }
  html, body { width: 1200px; height: 1200px; overflow: hidden; background: var(--stage); }
  .canvas { position: relative; width: 1200px; height: 1200px; display: flex; align-items: center; justify-content: center; }
  .billboard { position: relative; width: 1200px; height: 400px; overflow: hidden; background: var(--ink); }
  .billboard__bg { position: absolute; inset: 0; }

  .brand { position: absolute; left: 36px; top: 22px; color: var(--silver);
    font-family: "Poppins", sans-serif; font-weight: 900; line-height: 1; }
  .brand__name { display: block; font-size: 82px; letter-spacing: -1px; text-transform: uppercase; }
  .brand__sub { display: block; font-size: 36px; text-align: right; letter-spacing: 2px; text-transform: uppercase; margin-top: -2px; }

  .tagline { position: absolute; left: 608px; top: 30px; color: var(--purple-bright);
    font-family: "Poppins", sans-serif; font-weight: 900; font-size: 27px; line-height: 1.08;
    text-transform: uppercase; letter-spacing: 0.5px; }

  .offers { position: absolute; left: 24px; top: 172px; width: 570px; }
  .offer { display: flex; align-items: center; justify-content: flex-end; margin-bottom: 10px; }
  .offer__label { text-align: right; color: var(--silver); font-family: "Poppins", sans-serif;
    font-weight: 800; font-size: 25px; line-height: 1.05; text-transform: uppercase;
    text-shadow: 2px 2px 0 #111; margin-right: 12px; }
  .offer__price { color: var(--silver); font-family: "Poppins", sans-serif; font-weight: 800;
    font-size: 72px; line-height: 1; letter-spacing: -2px; text-shadow: 3px 3px 0 #111; }

  .truck-photo { position: absolute; left: 610px; top: 168px; width: 340px; height: 200px; }

  .schedule { position: absolute; left: 962px; top: 326px; display: flex; align-items: flex-end;
    color: var(--ink); font-family: "Poppins", sans-serif; font-weight: 800; line-height: 1; }
  .schedule__service { display: flex; flex-direction: column; }
  .schedule__small { font-size: 16px; }
  .schedule__big { font-size: 30px; letter-spacing: -1px; }
  .schedule__count { color: var(--purple); font-size: 62px; margin: 0 4px; line-height: 0.85; }
  .schedule__days { font-size: 17px; line-height: 1.05; padding-bottom: 4px; }
</style>
</head>
<body>
<div class="canvas">
  <section class="billboard">
    <svg class="billboard__bg" width="1200" height="400" viewBox="0 0 1200 400" aria-hidden="true">
      <defs>
        <linearGradient id="purpleFade" x1="0" y1="0" x2="0" y2="1">
          <stop offset="0" stop-color="#2f1644"/>
          <stop offset="1" stop-color="#5b2a86"/>
        </linearGradient>
        <linearGradient id="panelFade" x1="0" y1="0" x2="1" y2="1">
          <stop offset="0" stop-color="#ececec"/>
          <stop offset="1" stop-color="#d4d4d4"/>
        </linearGradient>
      </defs>
      <rect width="1200" height="400" fill="#0b0b0c"/>
      <polygon points="0,150 620,172 960,182 960,400 0,400" fill="url(#purpleFade)"/>
      <polygon points="915,0 1200,0 1200,400 968,400" fill="url(#panelFade)"/>
    </svg>

    <div class="brand">
      <span class="brand__name">Copperfox</span>
      <span class="brand__sub">Dumpsters</span>
    </div>

    <div class="tagline">Best<br>Prices in<br>Sevier<br>County</div>

    <div class="offers">
      <div class="offer">
        <div class="offer__label">30-Yard Dumpsters<br>Starting at</div>
        <div class="offer__price">600.00</div>
      </div>
      <div class="offer">
        <div class="offer__label">16-Yard Dumpsters<br>Starting at</div>
        <div class="offer__price">300.00</div>
      </div>
    </div>

    <svg class="truck-photo" viewBox="0 0 340 200" role="img" aria-label="Photo of white roll-off truck carrying a purple dumpster, bursting through a cracked wall">
      <defs>
        <linearGradient id="truckTone" x1="0" y1="0" x2="1" y2="0">
          <stop offset="0" stop-color="#e6e6e6"/>
          <stop offset="0.45" stop-color="#b9b9bd"/>
          <stop offset="0.75" stop-color="#4a2a66"/>
          <stop offset="1" stop-color="#9a9a9a"/>
        </linearGradient>
      </defs>
      <rect width="340" height="200" rx="6" fill="url(#truckTone)" opacity="0.9"/>
    </svg>

    <div class="schedule">
      <div class="schedule__service">
        <span class="schedule__small">Delivery &amp;</span>
        <span class="schedule__big">Pickup</span>
      </div>
      <span class="schedule__count">7</span>
      <span class="schedule__days">Days<br>a week</span>
    </div>
  </section>
</div>
</body>
</html>
```